Twitter Design Project

International Travel agent, need a twitter design. We romote family travel destinations, Marloft, Kestrane Studios, and cruises.

Travel

```html
<!DOCTYPE html>
<html lang="en">
<head>
<meta charset="utf-8">
<title>Wander Nest Trips – Profile Background</title>
<link rel="stylesheet" href="https://fonts.googleapis.com/css2?family=Luckiest+Guy&family=Arimo:wght@400&display=swap">
<style>
  :root {
    --page-bg: #e9eef0;
    --sky-white: #f4fbfe;
    --sky-pale: #c8ecf8;
    --sky-mid: #7fd0f0;
    --sky-deep: #1f6fe0;
    --brand-blue: #1d5fae;
    --ghost-text: rgba(180, 228, 248, 0.75);
    --ghost-edge: rgba(255, 255, 255, 0.55);
    --side-text: rgba(120, 190, 240, 0.55);
    --social-blue: #2a9fd8;
    --url-blue: #1f63b5;
    --photo-frame: #ffffff;
  }
  html, body {
    margin: 0;
    padding: 0;
    width: 1200px;
    height: 829px;
    overflow: hidden;
    background: var(--page-bg);
  }
  .profile-background {
    position: absolute;
    left: 0;
    top: 61px;
    width: 1200px;
    height: 706px;
    overflow: hidden;
    background: linear-gradient(90deg, var(--sky-white) 0%, var(--sky-pale) 22%, var(--sky-mid) 48%, #6cc3ee 72%, var(--sky-deep) 100%);
  }
  .cloud-layer {
    position: absolute;
    inset: 0;
    background:
      radial-gradient(ellipse 280px 150px at 740px 520px, rgba(255,255,255,0.75), transparent 70%),
      radial-gradient(ellipse 230px 170px at 1090px 120px, rgba(255,255,255,0.7), transparent 70%),
      radial-gradient(ellipse 320px 150px at 930px 650px, rgba(255,255,255,0.6), transparent 70%),
      radial-gradient(ellipse 210px 130px at 1130px 500px, rgba(255,255,255,0.55), transparent 70%);
  }
  .brand-mark {
    position: absolute;
    left: 10px;
    top: 52px;
    width: 190px;
    margin: 0;
    font-family: "Luckiest Guy", "Arial Black", sans-serif;
    font-weight: 400;
    font-size: 30px;
    line-height: 32px;
    color: var(--brand-blue);
    text-align: center;
  }
  .brand-mark .dot {
    display: block;
    width: 40px;
    height: 40px;
    margin: 0 auto 10px;
    border-radius: 50%;
    background: var(--brand-blue);
  }
  .photo-stack {
    position: absolute;
    left: 34px;
    top: 212px;
    width: 130px;
    height: 360px;
  }
  .photo {
    position: absolute;
    width: 70px;
    height: 74px;
    padding: 6px 6px 16px;
    background: var(--photo-frame);
    box-shadow: 0 2px 5px rgba(0,0,0,0.3);
  }
  .photo .scene { width: 100%; height: 100%; }
  .photo.resort { left: 42px; top: 0; transform: rotate(-8deg); }
  .photo.resort .scene { background: linear-gradient(160deg, #7ab7e0, #b9a27a 60%, #4f7a4a); }
  .photo.park { left: 2px; top: 64px; transform: rotate(-4deg); }
  .photo.park .scene { background: linear-gradient(180deg, #5aa0e0, #c85a4a 60%, #d8c8a0); }
  .photo.tower { left: 32px; top: 128px; transform: rotate(-12deg); }
  .photo.tower .scene { background: linear-gradient(180deg, #8ec7ee, #c9c2a8 65%, #6e8f4e); }
  .photo.beach { left: 2px; top: 188px; transform: rotate(-3deg); }
  .photo.beach .scene { background: linear-gradient(180deg, #4aa7e6, #2e8bc4 55%, #e9dcb6); }
  .photo.waterpark { left: 36px; top: 250px; transform: rotate(-6deg); }
  .photo.waterpark .scene { background: linear-gradient(180deg, #5fbde8, #d98d52 60%, #3e86b8); }
  .social-handle {
    position: absolute;
    left: 14px;
    top: 636px;
    margin: 0;
    display: flex;
    align-items: center;
    gap: 8px;
    font-family: "Arimo", sans-serif;
    font-size: 30px;
    line-height: 36px;
    color: var(--brand-blue);
  }
  .social-handle .social-dot {
    width: 26px;
    height: 26px;
    border-radius: 50%;
    background: var(--social-blue);
  }
  .site-url {
    position: absolute;
    left: 14px;
    top: 676px;
    margin: 0;
    font-family: "Arimo", sans-serif;
    font-size: 20px;
    line-height: 24px;
    color: var(--url-blue);
  }
  .ghost-title {
    position: absolute;
    left: 240px;
    top: 322px;
    width: 720px;
    margin: 0;
    text-align: center;
    font-family: "Luckiest Guy", "Arial Black", sans-serif;
    font-weight: 400;
    font-size: 96px;
    line-height: 104px;
    color: var(--ghost-text);
    -webkit-text-stroke: 2px var(--ghost-edge);
  }
  .ghost-side {
    position: absolute;
    left: 1030px;
    top: 68px;
    height: 570px;
    margin: 0;
    writing-mode: vertical-rl;
    text-align: center;
    font-family: "Luckiest Guy", "Arial Black", sans-serif;
    font-weight: 400;
    font-size: 60px;
    line-height: 68px;
    color: var(--side-text);
    -webkit-text-stroke: 2px rgba(255,255,255,0.35);
  }
</style>
</head>
<body>
  <main class="profile-background">
    <div class="cloud-layer" role="img" aria-label="Soft white clouds drifting across a blue sky"></div>

    <h1 class="brand-mark"><span class="dot"></span>WANDER<br>NEST TRIPS</h1>

    <div class="photo-stack">
      <div class="photo resort"><div class="scene" role="img" aria-label="Snapshot of a resort hotel by the pool"></div></div>
      <div class="photo park"><div class="scene" role="img" aria-label="Snapshot of a theme park street"></div></div>
      <div class="photo tower"><div class="scene" role="img" aria-label="Snapshot of a famous iron tower landmark"></div></div>
      <div class="photo beach"><div class="scene" role="img" aria-label="Snapshot of a tropical beach with a sailboat"></div></div>
      <div class="photo waterpark"><div class="scene" role="img" aria-label="Snapshot of a water park with slides"></div></div>
    </div>

    <p class="social-handle"><span class="social-dot"></span>@wandernest</p>
    <p class="site-url">Wandernesttrips.com</p>

    <p class="ghost-title">WANDER<br>NEST TRIPS</p>
    <p class="ghost-side">WANDER<br>NEST TRIPS</p>
  </main>
</body>
</html>
```